Tallowmere Editing Services (TEServices-hub.net)

We need a Wordpress-based site designed for a client who provides writing and editing services for the IT industry. We have a wireframe complete for the homepage, but need all internal pages designed (based on homepage wireframe) and the entire site coded for WP.

Internal pages include: "Our Work" (with samples & testimonials); "Capabilities" (with sections to address "strategy", "coaching", "writing" and "editing"); "About Us"; and a Contact page.

Will provide all copywriting, writing samples, testimonials, and client logos.

We completely realize/acknowledge the subject matter is visually BORING! Anything at all that can be done to make it look visually appealing would be *great*! Stock photography is fine.

Please feel free to ask any questions whatsoever. Thanks for your time!

```html
<!DOCTYPE html>
<html lang="en">
<head>
<meta charset="utf-8">
<title>Tallowmere Editing Services – Homepage Concepts</title>
<link href="https://fonts.googleapis.com/css2?family=Cinzel:wght@400;700&family=Roboto:wght@400;500;700&family=Heebo:wght@400;500&display=swap" rel="stylesheet">
<style>
:root{
  --blue:#1f4e96;
  --navy:#14285a;
  --deep:#0d1c45;
  --orange:#e8461c;
  --ink:#222;
  --muted:#666;
}
*{box-sizing:border-box;margin:0;padding:0}
html,body{width:985px;height:1200px;overflow:hidden}
body{background:radial-gradient(circle at 50% 40%,#9a9a9a,#7a7a7a);font-family:'Roboto',sans-serif;color:var(--ink);position:relative}
.page{position:absolute;top:33px;width:718px;background:#fff;transform-origin:0 0;transform:scale(.5674);box-shadow:0 6px 30px rgba(0,0,0,.45);overflow:hidden}
.page--a{left:69px;height:1997px}
.page--b{left:508px;height:1959px}
section,header,footer{position:relative}
.btn{display:flex;align-items:center;justify-content:center;background:var(--blue);color:#fff;font-weight:500;text-transform:uppercase;position:absolute}

/* header */
.site-header{height:59px}
.brand{position:absolute;left:86px;top:7px}
.brand-name{font-family:'Cinzel',serif;font-weight:700;font-size:23px;color:#1b1b24;line-height:27px;letter-spacing:-.3px}
.brand-tag{font-size:12.5px;font-weight:500;color:var(--orange);letter-spacing:.3px;line-height:14px}
.nav{position:absolute;left:292px;top:25px;display:flex;gap:16px;font-size:7.5px;font-weight:500;text-transform:uppercase}
.nav .is-current{border-bottom:1px solid var(--orange);padding-bottom:2px}
.nav-contact{left:558px;top:15px;width:74px;height:27px;font-size:7.5px}

/* hero */
.hero{height:318px;background:linear-gradient(120deg,#4d4f55 0%,#8a8a88 35%,#6c6f74 60%,#2f3238 100%)}
.hero-overlay{position:absolute;left:86px;top:73px;width:284px;height:245px;background:rgba(150,150,150,.35)}
.hero-title{position:absolute;left:112px;top:93px;font-family:'Cinzel',serif;font-size:24px;line-height:36px;color:#fff;text-shadow:0 1px 3px rgba(0,0,0,.4)}
.hero-cta{left:112px;top:255px;width:106px;height:33px;font-size:11px}
.hero-dots{position:absolute;left:678px;top:140px;display:flex;flex-direction:column;gap:8px}
.hero-dots span{width:4px;height:4px;border-radius:50%;background:#fff}
.hero-dots span:first-child{background:var(--orange)}

/* section titles */
.sec-title{position:absolute;left:0;right:0;text-align:center;font-family:'Cinzel',serif;font-size:25px;line-height:34px}
.t-blue{color:var(--blue)}
.t-navy{color:var(--navy)}
.t-orange{color:var(--orange)}

/* offer */
.offer{height:421px}
.offer .sec-title{top:52px}
.offer-grid{position:absolute;left:86px;top:113px;width:546px;display:grid;grid-template-columns:repeat(4,1fr);gap:7px}
.photo{display:block;width:100%}
.offer-item .photo{height:100px}
.offer-label{margin-top:18px;font-size:9px;font-weight:500}
.offer-text{margin-top:8px;font-size:6.3px;line-height:12.3px;color:var(--muted);width:110px}
.offer-cta{left:295px;top:343px;width:128px;height:26px;font-size:7.5px}

/* clients */
.clients{height:263px;background:linear-gradient(180deg,#0f1f4d,#0b1a40)}
.clients .sec-title{top:45px}
.client-row{position:absolute;left:88px;top:145px;display:flex;gap:11px}
.client-logo{width:127px;height:63px;background:#fff;display:flex;align-items:center;justify-content:center;gap:5px;font-size:17px;color:#222}
.client-logo i{width:9px;height:9px;border-radius:50%;background:#333}
.arrow{position:absolute;top:163px;width:24px;height:24px;border:1px solid rgba(255,255,255,.4);border-radius:50%}
.arrow svg{display:block}

/* work */
.work{height:498px;background:linear-gradient(135deg,#e9e4de 0%,#f6f4f2 45%,#dde3ea 100%)}
.work .sec-title{top:57px}
.work-grid{position:absolute;left:86px;top:159px;display:flex;gap:17px}
.work-card{width:171px;height:224px;background:#fff;border:1px solid #ccc}
.work-card .photo{height:100px}
.work-body{padding:14px 0 0 19px}
.work-head{font-size:8px;font-weight:500;margin-top:7px}
.work-text{margin-top:8px;font-size:6.2px;line-height:12.3px;color:var(--muted);width:136px}
.work-brand{margin-top:9px;display:flex;align-items:center;gap:4px;font-size:7.5px;font-weight:700}
.work-brand i{width:8px;height:8px;background:#111}
.work-cta{left:295px;top:420px;width:128px;height:26px;font-size:7.5px}

/* contact band */
.connect{height:226px;display:flex}
.connect-left{width:359px;background:linear-gradient(135deg,#1d4aa0,#173e8c);position:relative}
.connect-right{width:359px;background:linear-gradient(135deg,#ee5a2b,#d9441c);position:relative}
.connect-notch{position:absolute;left:339px;top:-1px;width:40px;height:12px}
.connect-msg{position:absolute;left:86px;top:54px;color:#fff;font-size:15px;font-weight:500;line-height:21.5px}
.connect-btn{position:absolute;left:86px;top:135px;width:77px;height:26px;background:#fff;color:var(--blue);font-size:7.5px;font-weight:500;display:flex;align-items:center;justify-content:center}
.news-msg{position:absolute;right:86px;top:54px;text-align:right;color:#fff;font-size:13px;font-weight:500;line-height:23px}
.news-input{position:absolute;left:59px;top:128px;width:213px;height:26px;background:#fff;font-size:7.5px;color:#333;padding-left:12px;display:flex;align-items:center}

/* footer A */
.footer-a{height:212px}
.footer-a .brand{top:25px}
.f-contact{position:absolute;left:86px;font-size:7px;color:#333;line-height:14.5px;display:flex;gap:10px;align-items:flex-start}
.f-contact svg{flex:none;margin-top:3px}
.f-col{position:absolute;top:29px;font-size:7px;color:#333}
.f-col h4{font-family:'Heebo',sans-serif;font-size:11px;font-weight:400;color:#111;margin-bottom:14px}
.f-col li{list-style:none;line-height:14.5px}
.social{display:flex;gap:8px}
.social li{display:flex;align-items:center;gap:2px;font-size:6px;color:var(--blue)}
.social li i{width:8px;height:8px;background:var(--blue)}
.f-rule{position:absolute;left:86px;right:86px;top:170px;border-top:1px solid #ddd}
.f-copy{position:absolute;left:0;right:0;top:188px;text-align:center;font-size:7px;color:#333}

/* footer B */
.footer-b{height:174px}
.fb-item{position:absolute;top:29px;display:flex;align-items:center;gap:10px;font-size:6.5px;line-height:12px;color:#444}
.fb-icon{width:26px;height:26px;border-radius:50%;border:1.5px solid var(--orange);display:flex;align-items:center;justify-content:center}
.fb-icon--fill{background:var(--orange)}
.fb-sep{position:absolute;top:30px;height:24px;border-left:1px solid #ddd}
.fb-rule{position:absolute;left:8px;right:8px;top:88px;border-top:1px solid #e3e3e3}
.fb-copy{position:absolute;left:0;right:0;top:107px;text-align:center;font-size:6.5px;color:#444}
.footer-b .social{position:absolute;left:0;right:0;top:138px;justify-content:center;gap:16px}
.footer-b .social li{font-size:7px}
.footer-b .social li i{width:11px;height:11px}
</style>
</head>
<body>

<!-- Concept A -->
<main class="page page--a">
  <header class="site-header">
    <div class="brand"><div class="brand-name">TALLOWMERE</div><div class="brand-tag">EDITING SERVICES</div></div>
    <nav class="nav"><span class="is-current">Home</span><span>Our Work</span><span>Capabilities</span><span>About Us</span><span>Blog</span></nav>
    <span class="btn nav-contact">Contact Us</span>
  </header>
  <section class="hero" role="img" aria-label="Photo of hands typing on a laptop keyboard">
    <div class="hero-overlay"></div>
    <h1 class="hero-title">COMMUNICATE<br>YOUR EXPERTISE &amp;<br>YOUR CUSTOMER<br>SUCCESSES</h1>
    <span class="btn hero-cta">Get Started</span>
    <div class="hero-dots"><span></span><span></span><span></span></div>
  </section>
  <section class="offer">
    <h2 class="sec-title"><span class="t-navy">WHAT</span> <span class="t-orange">WE OFFER</span></h2>
    <div class="offer-grid">
      <div class="offer-item"><div class="photo" role="img" aria-label="Photo of a strategy sketch beside a laptop" style="background:linear-gradient(135deg,#3a3530,#8a7a66)"></div><div class="offer-label">STRATEGY</div><p class="offer-text">Lorem ipsum doltconsectetur adipiscing d do eiusmod tempor incididunt ut labore et dolore magna aliq ipsum suspendisse ultrices gravidausodo</p></div>
      <div class="offer-item"><div class="photo" role="img" aria-label="Photo of a team gathered around a table" style="background:linear-gradient(135deg,#4a5a4a,#b8b8b2)"></div><div class="offer-label">COACHING</div><p class="offer-text">Lorem ipsum doltconsectetur adipiscing d do eiusmod tempor incididunt ut labore et dolore magna aliq ipsum suspendisse ultrices gravidausodo</p></div>
      <div class="offer-item"><div class="photo" role="img" aria-label="Photo of a laptop in warm light" style="background:linear-gradient(135deg,#d9b58a,#6a5448)"></div><div class="offer-label">WRITING</div><p class="offer-text">Lorem ipsum doltconsectetur adipiscing d do eiusmod tempor incididunt ut labore et dolore magna aliq ipsum suspendisse ultrices gravidausodo</p></div>
      <div class="offer-item"><div class="photo" role="img" aria-label="Photo of a person working at computer screens" style="background:linear-gradient(135deg,#2e3a44,#8a98a4)"></div><div class="offer-label">EDITING</div><p class="offer-text">Lorem ipsum doltconsectetur adipiscing d do eiusmod tempor incididunt ut labore et dolore magna aliq ipsum suspendisse ultrices gravidausodo</p></div>
    </div>
    <span class="btn offer-cta">View Our Capabilities</span>
  </section>
  <section class="clients">
    <h2 class="sec-title"><span class="t-blue">A SELECTION OF</span><br><span class="t-orange">PAST AND CURRENT CLIENTS</span></h2>
    <span class="arrow" style="left:45px"><svg width="22" height="22"><path d="M13 7l-4 4 4 4" stroke="#fff" fill="none"/></svg></span>
    <div class="client-row">
      <div class="client-logo"><i></i>Nerivo</div>
      <div class="client-logo"><i></i>Caldrith</div>
      <div class="client-logo"><i></i>Ombrelin</div>
      <div class="client-logo"><i></i>Felvasko</div>
    </div>
    <span class="arrow" style="left:649px"><svg width="22" height="22"><path d="M9 7l4 4-4 4" stroke="#fff" fill="none"/></svg></span>
  </section>
  <section class="work">
    <h2 class="sec-title"><span class="t-blue">TEXT HIGHLIGHTING</span><br><span class="t-orange">THE TYPE OF WORK YOU DO</span></h2>
    <div class="work-grid">
      <article class="work-card"><div class="photo" role="img" aria-label="Photo of a person working on a laptop" style="background:linear-gradient(135deg,#c9c9c4,#6a6560)"></div><div class="work-body"><h3 class="work-head">SED UT PERSPICIATIS UNDENI</h3><p class="work-text">Lorem ipsum dolor sit amet, consectetur adipiscing elit, sed do eiusmod tempor incididunt ut labore et dolore magna aliquauis ipsum suspendisse</p><div class="work-brand"><i></i>Dunmarrow</div></div></article>
      <article class="work-card"><div class="photo" role="img" aria-label="Photo of hands on a laptop" style="background:linear-gradient(135deg,#8a6a4e,#d4b596)"></div><div class="work-body"><h3 class="work-head">EXCEPTEUR SINT OCCAECAT</h3><p class="work-text">Lorem ipsum dolor sit amet, consectetur adipiscing elit, sed do eiusmod tempor incididunt ut labore et dolore magna aliquauis ipsum suspendisse</p><div class="work-brand"><i></i>Keltrina</div></div></article>
      <article class="work-card"><div class="photo" role="img" aria-label="Photo of a hand writing on paper" style="background:linear-gradient(135deg,#5c6f86,#e6e2de)"></div><div class="work-body"><h3 class="work-head">UT ENIM AD MINIM VENIAM</h3><p class="work-text">Lorem ipsum dolor sit amet, consectetur adipiscing elit, sed do eiusmod tempor incididunt ut labore et dolore magna aliquauis ipsum suspendisse</p><div class="work-brand"><i></i>Dunmarrow</div></div></article>
    </div>
    <span class="btn work-cta">View Our Work</span>
  </section>
  <section class="connect">
    <div class="connect-left"><p class="connect-msg">Feel free to contact<br>us with any questions.<br>We're happy to help.</p><span class="connect-btn">GET IN TOUCH</span></div>
    <div class="connect-right"><p class="news-msg">Editorial inspiration delivered<br>straight to your inbox.</p><span class="news-input">Enter email</span></div>
    <svg class="connect-notch" viewBox="0 0 40 12"><path d="M0 0h40c-8 0-12 10-20 10S8 0 0 0z" fill="#fff"/><path d="M17 6l3-3 3 3" stroke="#bbb" fill="none"/></svg>
  </section>
  <footer class="footer-a">
    <div class="brand"><div class="brand-name">TALLOWMERE</div><div class="brand-tag">EDITING SERVICES</div></div>
    <div class="f-contact" style="top:76px"><svg width="7" height="9"><path d="M3.5 0a3.5 3.5 0 0 1 3.5 3.5C7 6 3.5 9 3.5 9S0 6 0 3.5A3.5 3.5 0 0 1 3.5 0z" fill="#111"/><circle cx="3.5" cy="3.5" r="1.2" fill="#fff"/></svg><span>Lorem ipsum dolor sit amet,<br>consectetur adipiscing elit, sed</span></div>
    <div class="f-contact" style="top:115px"><svg width="8" height="8"><path d="M1 0l2 0 1 2-1 1q1 2 2 2l1-1 2 1v2q-1 1-2 1Q1 7 0 2q0-1 1-2z" fill="#111"/></svg><span>(555) 010 4477</span></div>
    <div class="f-contact" style="top:139px"><svg width="9" height="7"><rect width="9" height="7" fill="#111"/><path d="M0 0l4.5 4L9 0" stroke="#fff" fill="none"/></svg><span>info@teservices-hub.net</span></div>
    <div class="f-col" style="left:281px"><h4>Quik Links</h4><ul><li>Home</li><li>OurWork</li><li>Capabilities</li><li>About Us</li><li>Blog</li></ul></div>
    <div class="f-col" style="left:406px"><h4>Company</h4><ul><li>Terms&amp;condtions</li><li>Privacy Policy</li><li>About Us</li><li>Support</li></ul></div>
    <div class="f-col" style="left:540px"><h4>Socil Links</h4><ul class="social"><li><i></i>Vorlu</li><li><i></i>Quippa</li><li><i></i>Glimzo</li><li><i></i>Tronvel</li></ul></div>
    <div class="f-rule"></div>
    <p class="f-copy">©Copyrights 2021 Company Name &nbsp;| &nbsp; All Rights Reserved</p>
  </footer>
</main>

<!-- Concept B -->
<main class="page page--b">
  <header class="site-header">
    <div class="brand"><div class="brand-name">TALLOWMERE</div><div class="brand-tag">EDITING SERVICES</div></div>
    <nav class="nav"><span class="is-current">Home</span><span>Our Work</span><span>Capabilities</span><span>About Us</span><span>Blog</span></nav>
    <span class="btn nav-contact">Contact Us</span>
  </header>
  <section class="hero" role="img" aria-label="Photo of hands typing on a laptop keyboard">
    <div class="hero-overlay"></div>
    <h1 class="hero-title">COMMUNICATE<br>YOUR EXPERTISE &amp;<br>YOUR CUSTOMER<br>SUCCESSES</h1>
    <span class="btn hero-cta">Get Started</span>
    <div class="hero-dots"><span></span><span></span><span></span></div>
  </section>
  <section class="offer">
    <h2 class="sec-title"><span class="t-navy">WHAT</span> <span class="t-orange">WE OFFER</span></h2>
    <div class="offer-grid">
      <div class="offer-item"><div class="photo" role="img" aria-label="Photo of a strategy sketch beside a laptop" style="background:linear-gradient(135deg,#3a3530,#8a7a66)"></div><div class="offer-label">STRATEGY</div><p class="offer-text">Lorem ipsum doltconsectetur adipiscing d do eiusmod tempor incididunt ut labore et dolore magna aliq ipsum suspendisse ultrices gravidausodo</p></div>
      <div class="offer-item"><div class="photo" role="img" aria-label="Photo of a team gathered around a table" style="background:linear-gradient(135deg,#4a5a4a,#b8b8b2)"></div><div class="offer-label">COACHING</div><p class="offer-text">Lorem ipsum doltconsectetur adipiscing d do eiusmod tempor incididunt ut labore et dolore magna aliq ipsum suspendisse ultrices gravidausodo</p></div>
      <div class="offer-item"><div class="photo" role="img" aria-label="Photo of a laptop in warm light" style="background:linear-gradient(135deg,#d9b58a,#6a5448)"></div><div class="offer-label">WRITING</div><p class="offer-text">Lorem ipsum doltconsectetur adipiscing d do eiusmod tempor incididunt ut labore et dolore magna aliq ipsum suspendisse ultrices gravidausodo</p></div>
      <div class="offer-item"><div class="photo" role="img" aria-label="Photo of a person working at computer screens" style="background:linear-gradient(135deg,#2e3a44,#8a98a4)"></div><div class="offer-label">EDITING</div><p class="offer-text">Lorem ipsum doltconsectetur adipiscing d do eiusmod tempor incididunt ut labore et dolore magna aliq ipsum suspendisse ultrices gravidausodo</p></div>
    </div>
    <span class="btn offer-cta">View Our Capabilities</span>
  </section>
  <section class="clients">
    <h2 class="sec-title"><span class="t-blue">A SELECTION OF</span><br><span class="t-orange">PAST AND CURRENT CLIENTS</span></h2>
    <span class="arrow" style="left:45px"><svg width="22" height="22"><path d="M13 7l-4 4 4 4" stroke="#fff" fill="none"/></svg></span>
    <div class="client-row">
      <div class="client-logo"><i></i>Nerivo</div>
      <div class="client-logo"><i></i>Caldrith</div>
      <div class="client-logo"><i></i>Ombrelin</div>
      <div class="client-logo"><i></i>Felvasko</div>
    </div>
    <span class="arrow" style="left:649px"><svg width="22" height="22"><path d="M9 7l4 4-4 4" stroke="#fff" fill="none"/></svg></span>
  </section>
  <section class="work">
    <h2 class="sec-title"><span class="t-blue">TEXT HIGHLIGHTING</span><br><span class="t-orange">THE TYPE OF WORK YOU DO</span></h2>
    <div class="work-grid">
      <article class="work-card"><div class="photo" role="img" aria-label="Photo of a person working on a laptop" style="background:linear-gradient(135deg,#c9c9c4,#6a6560)"></div><div class="work-body"><h3 class="work-head">SED UT PERSPICIATIS UNDENI</h3><p class="work-text">Lorem ipsum dolor sit amet, consectetur adipiscing elit, sed do eiusmod tempor incididunt ut labore et dolore magna aliquauis ipsum suspendisse</p><div class="work-brand"><i></i>Dunmarrow</div></div></article>
      <article class="work-card"><div class="photo" role="img" aria-label="Photo of hands on a laptop" style="background:linear-gradient(135deg,#8a6a4e,#d4b596)"></div><div class="work-body"><h3 class="work-head">EXCEPTEUR SINT OCCAECAT</h3><p class="work-text">Lorem ipsum dolor sit amet, consectetur adipiscing elit, sed do eiusmod tempor incididunt ut labore et dolore magna aliquauis ipsum suspendisse</p><div class="work-brand"><i></i>Keltrina</div></div></article>
      <article class="work-card"><div class="photo" role="img" aria-label="Photo of a hand writing on paper" style="background:linear-gradient(135deg,#5c6f86,#e6e2de)"></div><div class="work-body"><h3 class="work-head">UT ENIM AD MINIM VENIAM</h3><p class="work-text">Lorem ipsum dolor sit amet, consectetur adipiscing elit, sed do eiusmod tempor incididunt ut labore et dolore magna aliquauis ipsum suspendisse</p><div class="work-brand"><i></i>Dunmarrow</div></div></article>
    </div>
    <span class="btn work-cta">View Our Work</span>
  </section>
  <section class="connect">
    <div class="connect-left"><p class="connect-msg">Feel free to contact<br>us with any questions.<br>We're happy to help.</p><span class="connect-btn">GET IN TOUCH</span></div>
    <div class="connect-right"><p class="news-msg">Editorial inspiration delivered<br>straight to your inbox.</p><span class="news-input">Enter email</span></div>
    <svg class="connect-notch" viewBox="0 0 40 12"><path d="M0 0h40c-8 0-12 10-20 10S8 0 0 0z" fill="#fff"/><path d="M17 6l3-3 3 3" stroke="#bbb" fill="none"/></svg>
  </section>
  <footer class="footer-b">
    <div class="fb-item" style="left:120px"><span class="fb-icon"><svg width="9" height="12"><path d="M4.5 1a3.5 3.5 0 0 1 3.5 3.5C8 7 4.5 11 4.5 11S1 7 1 4.5A3.5 3.5 0 0 1 4.5 1z" fill="none" stroke="#e8461c" stroke-width="1.3"/><circle cx="4.5" cy="4.5" r="1.2" fill="#e8461c"/></svg></span><span>122,Ut enim ad minim veniam<br>xercitation ullamco</span></div>
    <span class="fb-sep" style="left:287px"></span>
    <div class="fb-item" style="left:318px"><span class="fb-icon fb-icon--fill"><svg width="11" height="11"><path d="M2 1h2l1 2.5-1.3 1q1 2 3 3l1-1.3L10 7v2q-1 1.5-2.5 1Q2 8.5 1 3.5 1 2 2 1z" fill="#fff"/></svg></span><span>Call Mara at<br>(555) 014-2287</span></div>
    <span class="fb-sep" style="left:472px"></span>
    <div class="fb-item" style="left:472px"><span class="fb-icon"><svg width="12" height="9"><rect x=".7" y=".7" width="10.6" height="7.6" fill="none" stroke="#e8461c" stroke-width="1.3"/><path d="M1 1l5 4 5-4" stroke="#e8461c" fill="none" stroke-width="1.2"/></svg></span><span>Email Us :<br>info@teservices-hub.net</span></div>
    <div class="fb-rule"></div>
    <p class="fb-copy">© 2021 Tallowmere editing services. All rights reserved &nbsp;| &nbsp;Privacy &nbsp;| &nbsp;Terms of Use</p>
    <ul class="social"><li><i></i>Vorlu</li><li><i></i>Quippa</li><li><i></i>Glimzo</li><li><i></i>Tronvel</li></ul>
  </footer>
</main>

</body>
</html>
```